BUSINESS CARD DESIGN

NAME- TODD MASVERIK
PHONE NUMER - 808- 451-7082
EMAIL- OFFICE@VORLINDE-GRADEWAY.COM
BACK OF CARD- SPEACIALIZES IN LAND CLEARING, FORESTRY MUCLHING AND EXCAVATION

Contact Information for Business Card

NAME- TODD MASVERIK PHONE NUMER - 808- 451-7082 EMAIL- OFFICE@VORLINDE-GRADEWAY.COM BACK OF CARD- SPEACIALIZES IN LAND CLEARING , MUCLHING AND EXCAVATION

```html
<!DOCTYPE html>
<html lang="en">
<head>
<meta charset="utf-8">
<title>Vorlinde Gradeway – Business Card</title>
<link href="https://fonts.googleapis.com/css2?family=Montserrat:wght@600;700&display=swap" rel="stylesheet">
<style>
  :root{
    --gold:#F9B51A;
    --white:#FFFFFF;
    --page:#FFFFFF;
    --shadow:rgba(0,0,0,.55);
  }
  *{margin:0;padding:0;box-sizing:border-box}
  html,body{width:1200px;height:1132px;overflow:hidden;background:var(--page);font-family:"Montserrat",sans-serif}
  .card{position:absolute;left:255px;width:690px;height:394px;overflow:hidden;box-shadow:22px 22px 26px var(--shadow)}
  .card-front{top:151px;background:var(--white)}
  .card-back{top:627px;background:var(--gold)}
  .wave{position:absolute;left:0;top:0;width:690px;height:80px}
  .brand{position:absolute;display:flex;flex-direction:column;align-items:center;text-align:center;font-weight:700}
  .brand-mark{border-radius:50%}
  .brand-name{letter-spacing:1px;line-height:1.25}
  .card-front .brand{left:50px;top:110px;width:210px;color:var(--gold)}
  .card-front .brand-mark{width:110px;height:110px;border:6px solid var(--gold);margin-bottom:14px}
  .card-front .brand-name{font-size:17px}
  .card-front .brand-phone{font-size:10px;letter-spacing:6px;margin-top:6px}
  .divider{position:absolute;left:321px;top:101px;width:3px;height:219px;background:var(--gold)}
  .person{position:absolute;left:376px;top:94px;color:var(--gold);font-weight:700}
  .person-name{font-size:30px;letter-spacing:.5px;line-height:1.1}
  .person-role{display:inline-block;font-size:23px;margin-top:2px;padding-bottom:2px;border-bottom:3px solid var(--gold)}
  .contacts{position:absolute;left:372px;top:214px;list-style:none;color:var(--gold);font-weight:700;font-size:16px}
  .contacts li{display:flex;align-items:center;height:40px}
  .contacts svg{width:26px;height:26px;margin-right:18px;flex:none}
  .card-back .brand{left:195px;top:62px;width:300px;color:var(--white)}
  .card-back .brand-mark{width:160px;height:160px;border:8px solid var(--white);margin-bottom:18px}
  .card-back .brand-name{font-size:24px}
  .card-back .brand-phone{font-size:12px;letter-spacing:9px;margin-top:8px}
  .tagline{position:absolute;left:0;right:0;top:346px;text-align:center;color:var(--white);font-weight:700;font-size:13.5px;letter-spacing:.8px}
</style>
</head>
<body>
  <section class="card card-front">
    <svg class="wave" viewBox="0 0 690 80" preserveAspectRatio="none" aria-hidden="true">
      <path d="M0 0 H690 V53 C560 40 470 42 360 58 C250 74 150 80 90 50 C50 32 20 14 0 0 Z" fill="var(--gold)"/>
    </svg>
    <div class="brand">
      <span class="brand-mark"></span>
      <span class="brand-name">VORLINDE GRADEWAY LLC</span>
      <span class="brand-phone">808-451-7082</span>
    </div>
    <span class="divider"></span>
    <div class="person">
      <div class="person-name">TODD MASVERIK</div>
      <div class="person-role">OWNER</div>
    </div>
    <ul class="contacts">
      <li>
        <svg viewBox="0 0 26 26"><rect x="1" y="6" width="24" height="15" fill="var(--gold)"/><path d="M1 6 L13 15 L25 6 M1 21 L10 13 M25 21 L16 13" stroke="#fff" stroke-width="1.6" fill="none"/></svg>
        @VORLINDE-GRADEWAY.COM
      </li>
      <li>
        <svg viewBox="0 0 26 26" fill="none" stroke="var(--gold)" stroke-width="1.6" stroke-linejoin="round"><path d="M6 3 L10 8 L8 11 C9 14 12 17 15 18 L18 16 L23 20 L20 24 C12 23 3 14 2 6 Z"/><path d="M15 3 A8 8 0 0 1 23 11 M15 7 A4 4 0 0 1 19 11"/></svg>
        +808- 451-7082
      </li>
      <li>
        <svg viewBox="0 0 26 26" fill="none" stroke="var(--gold)" stroke-width="1.5"><circle cx="13" cy="13" r="11"/><ellipse cx="13" cy="13" rx="5" ry="11"/><path d="M2 13 H24 M4 7 H22 M4 19 H22"/></svg>
        www.vorlinde-gradeway.com
      </li>
    </ul>
  </section>

  <section class="card card-back">
    <div class="brand">
      <span class="brand-mark"></span>
      <span class="brand-name">VORLINDE GRADEWAY LLC</span>
      <span class="brand-phone">808-451-7082</span>
    </div>
    <p class="tagline">SPEACIALIZES IN LAND CLEARING , MUCLHING AND EXCAVATION</p>
  </section>
</body>
</html>
```